Kem7Dex Letterhead

Need a new letterhead for my law firm.
IDENTIFYING INFORMATION BELOW:
Ansel T Brightwater III
Attorney at Law
Address: 4832 Tillbury Rd, Ste 250, Dallas, TX 75204
Phone: 866-402-7183
Fax: 469-583-0271
Email: kem@kem7dex.example
Website: www.kem7dex.example

Colors
0054AA
0677BA
7BADD7
CADEEF
E8F1F8

Requirements
Must have
• Logo needs to be on the letterhead, along with identifying information which is included in the project description.

```html
<!DOCTYPE html>
<html lang="en">
<head>
<meta charset="utf-8">
<title>Kem7Dex Letterhead</title>
<link href="https://fonts.googleapis.com/css2?family=Montserrat:wght@300;400;500;600;800&family=Roboto+Condensed:wght@400&display=swap" rel="stylesheet">
<style>
  :root {
    --ink: #060709;
    --brand-blue: #0F73B2;
    --paper: #ffffff;
    --backdrop: #e6e6e8;
    --pattern-tint: #fafafa;
  }
  * { margin: 0; padding: 0; box-sizing: border-box; }
  html, body {
    width: 904px;
    height: 1200px;
    overflow: hidden;
    background: var(--backdrop);
  }
  .letterhead {
    position: absolute;
    left: 28px;
    top: 0;
    width: 848px;
    height: 1200px;
    background: var(--paper);
    color: var(--ink);
    overflow: hidden;
  }
  .background-pattern {
    position: absolute;
    inset: 0;
    background: var(--pattern-tint);
  }
  .header-bar {
    position: absolute;
    left: 0;
    top: 43px;
    width: 413px;
    height: 62px;
    background: var(--ink);
  }
  .header-accent {
    position: absolute;
    left: 777px;
    top: 43px;
    width: 71px;
    height: 62px;
    background: var(--brand-blue);
  }
  .brand-name {
    position: absolute;
    left: 428px;
    top: 32px;
    width: 340px;
    text-align: center;
    font-family: "Montserrat", sans-serif;
    font-weight: 800;
    font-size: 47px;
    letter-spacing: 1px;
    line-height: 1;
    text-transform: uppercase;
    white-space: nowrap;
  }
  .tagline {
    position: absolute;
    left: 428px;
    top: 85px;
    width: 340px;
    text-align: center;
    font-family: "Montserrat", sans-serif;
    font-weight: 300;
    font-size: 20px;
    letter-spacing: 2.5px;
    line-height: 1;
    text-transform: uppercase;
    white-space: nowrap;
  }
  .attorney {
    position: absolute;
    right: 89px;
    top: 119px;
    text-align: right;
    font-family: "Montserrat", sans-serif;
    line-height: 25px;
    font-size: 22px;
    white-space: nowrap;
  }
  .attorney-name { font-weight: 600; }
  .attorney-title { font-weight: 400; }
  .contact {
    position: absolute;
    right: 89px;
    top: 175px;
    text-align: right;
    font-family: "Roboto Condensed", sans-serif;
    font-size: 14.5px;
    line-height: 20.5px;
    list-style: none;
    white-space: nowrap;
  }
  .footer-accent {
    position: absolute;
    left: 0;
    top: 1174px;
    width: 71px;
    height: 26px;
    background: var(--brand-blue);
  }
  .footer-bar {
    position: absolute;
    left: 78px;
    top: 1174px;
    width: 770px;
    height: 26px;
    background: var(--ink);
  }
</style>
</head>
<body>
  <main class="letterhead">
    <div class="background-pattern" role="img" aria-label="Faint repeating brand name pattern across the page"></div>
    <div class="header-bar"></div>
    <div class="header-accent"></div>
    <div class="brand-name">Kem7Dex</div>
    <div class="tagline">Counsel you trust</div>
    <div class="attorney">
      <div class="attorney-name">ANSEL T BRIGHTWATER III</div>
      <div class="attorney-title">ATTORNEY AT LAW</div>
    </div>
    <ul class="contact">
      <li>4832 Tillbury Rd, Ste 250, Dallas, TX 75204</li>
      <li>Phone: 866-402-7183</li>
      <li>Fax: 469-583-0271</li>
      <li>Email: kem@kem7dex.example</li>
      <li>Website: www.kem7dex.example</li>
    </ul>
    <div class="footer-accent"></div>
    <div class="footer-bar"></div>
  </main>
</body>
</html>
```